TRU Staffing DL Flyer

Tru staffing needs a glossy brochure designed for an upcoming VIP event of our clients which are real estate agencies.

Background:
Tru Staffing specialises in Realestate recruitment in Australia. We have been in the Realestate Recruitment industry for 18 years and are the highest referred agency in the Brisbane Market. We Recruit Property Managers, Commercial and Residential, Sales and support staff for our clients.

Guideline:
- The flyer will be DL size (210x99mm)
- We would like to see designs that use the colors Green and Black same as our logo (attached)
- We would like something modern with a sleek corporate feel
- Need to include other information as detailed below in the "Must have" section
Updates

My logo and contact details is a must on the DHL flyer

Design is up to you

Kind Regards

Leon

Reason: Hi Designers Thank you for your help it is a very hard decision that is why I have made 1. prize $160 and 2. prize $100 and extended the deadline until Wednesday. Kind Regards Leon

Target Market(s)

Residential and Commercial Realestate firms in Australia

Industry/Entity Type

Real Estate

Requirements
Must have
• Why clients use TRU:
With extensive years of recruitment experience we are the highest referred recruitment company in the Brisbane market.“Our clients benefit from our wealth of experience and knowledge within their industry to recruit the right candidate.”

- Why Candidates use TRU:
“With our long standing experience within recruitment , we take the time and care attitude to find the right position and culture suityour working experience."

- Tru Logo
- Website details: www.trustaffing.com.au
- Contact details:
Leon Ashford
Recruitment Manager
Mb: 0412 583 216
Ph: 3715 2649
Fax: 3715 2687
E: leon@trustaffing.com.au
Level 1/ 142 Harlow Street, Fernvale QLD 4306
Nice to have
• - Why Tru does quality and background checks on candidates
- The advantage of using Tru Staffing vs Recruitment on your own
- 12 week Guarantee period on all placements

```html
<!DOCTYPE html>
<html lang="en">
<head>
<meta charset="utf-8">
<title>TRU Staffing DL Flyer</title>
<link rel="stylesheet" href="https://fonts.googleapis.com/css2?family=Open+Sans:wght@400;600;700&display=swap">
<style>
  :root {
    --stage: #3d3d3d;
    --paper: #ffffff;
    --green: #6db33f;
    --ink: #1e1e1e;
    --accent: #f05a28;
    --white: #ffffff;
  }
  * { margin: 0; padding: 0; box-sizing: border-box; }
  html, body {
    width: 1200px;
    height: 1181px;
    overflow: hidden;
    background: var(--stage);
    font-family: "Open Sans", Arial, sans-serif;
    color: var(--ink);
  }
  .flyer {
    position: absolute;
    width: 468px;
    height: 910px;
    background: var(--paper);
    overflow: hidden;
  }
  .flyer--front { left: 138px; top: 90px; }
  .flyer--back  { left: 636px; top: 170px; }

  /* brand name */
  .brand {
    position: absolute;
    left: 0; right: 0;
    text-align: center;
    font-weight: 700;
    color: var(--ink);
    white-space: nowrap;
  }
  .flyer--front .brand { top: 120px; font-size: 52px; }
  .flyer--back .brand { top: 486px; font-size: 36px; }

  /* front sections */
  .section-tab {
    position: absolute;
    left: 0;
    width: 338px;
    height: 40px;
    padding-left: 18px;
    background: var(--green);
    border-radius: 0 12px 12px 0;
    color: var(--white);
    font-size: 19px;
    font-weight: 600;
    line-height: 40px;
  }
  .section-tab--clients { top: 356px; }
  .section-tab--candidates { top: 548px; }
  .section-body {
    position: absolute;
    left: 14px;
    right: 18px;
    font-size: 16px;
    line-height: 21px;
    color: var(--ink);
  }
  .section-body--clients { top: 406px; }
  .section-body--candidates { top: 598px; }

  .footer-band {
    position: absolute;
    left: 0; right: 0; bottom: 0;
    height: 80px;
    background: var(--green);
  }
  .web {
    position: absolute;
    right: 18px;
    color: var(--white);
    font-size: 16px;
  }
  .flyer--front .web { bottom: 24px; }

  /* back panel */
  .selling-point {
    position: absolute;
    left: 0; right: 0;
    text-align: center;
  }
  .selling-point__title {
    color: var(--accent);
    font-size: 33px;
    font-weight: 600;
    line-height: 40px;
    white-space: nowrap;
  }
  .selling-point__sub {
    font-size: 19px;
    font-weight: 600;
    line-height: 22px;
  }
  .selling-point--checks { top: 86px; }
  .selling-point--advantage { top: 214px; }
  .selling-point--guarantee { top: 352px; }

  .contact-panel {
    position: absolute;
    left: 0; top: 620px;
    width: 468px; height: 290px;
  }
  .contact {
    position: absolute;
    right: 36px;
    top: 678px;
    text-align: right;
    color: var(--white);
    font-size: 16px;
    line-height: 21px;
    font-style: normal;
  }
  .contact__name { font-size: 21px; font-weight: 600; line-height: 26px; }
  .contact__role { font-size: 16px; font-weight: 600; margin-bottom: 22px; }
  .flyer--back .web { bottom: 24px; right: 26px; }
</style>
</head>
<body>

<section class="flyer flyer--front">
  <div class="brand">TRU Staffing</div>

  <h2 class="section-tab section-tab--clients">WHY CLIENTS USE TRU:</h2>
  <p class="section-body section-body--clients">With extensive years of recruitment experience we are the highest referred recruitment company in the Brisbane market.“Our clients benefit from our wealth of experience and knowledge within their industry to recruit the right candidate.”</p>

  <h2 class="section-tab section-tab--candidates">WHY CANDIDATES USE TRU:</h2>
  <p class="section-body section-body--candidates">“With our long standing experience within recruitment , we take the time and care attitude to find the right position and culture suityour working experience."</p>

  <div class="footer-band"></div>
  <p class="web">www.trustaffing.com.au</p>
</section>

<section class="flyer flyer--back">
  <div class="selling-point selling-point--checks">
    <p class="selling-point__title">Why Tru does quality</p>
    <p class="selling-point__sub">and background checks on candidates</p>
  </div>
  <div class="selling-point selling-point--advantage">
    <p class="selling-point__title">The advantage of using Tru</p>
    <p class="selling-point__sub">Staffing vs Recruitment on your own</p>
  </div>
  <div class="selling-point selling-point--guarantee">
    <p class="selling-point__title">12 week Guarantee</p>
    <p class="selling-point__sub">period on all placements</p>
  </div>

  <div class="brand">TRU Staffing</div>

  <svg class="contact-panel" viewBox="0 0 468 290" aria-hidden="true">
    <path d="M0 290 V70 Q0 10 60 8 Q260 0 468 14 V290 Z" fill="var(--green)"/>
  </svg>

  <address class="contact">
    <p class="contact__name">Leon Ashford</p>
    <p class="contact__role">Recruitment Manager</p>
    <p>Mb: 0412 583 216</p>
    <p>Ph: 3715 2649</p>
    <p>Fax: 3715 2687</p>
    <p>E: leon@trustaffing.com.au</p>
    <p>Level 1/ 142 Harlow Street, Fernvale QLD 4306</p>
  </address>
  <p class="web">www.trustaffing.com.au</p>
</section>

</body>
</html>
```